Kelvane Plumbing Business cards

Company is Kelvane Plumbing.
name Dashel Morrowby, I am a plumber, drainer, gasfitter and roofer
Mobile: 0431 906 154
Email address: info@kelvaneplumbing.example (check out my website for some ideas)
Website: www.kelvaneplumbing.example
ABN: 82 916 203 471
LIC: 604517K

I am reliable all round plumber. I am a 24 hour emergency service. Kelvane Plumbing is a professional plumbing service in the Illawarra, South Coast, Southern Sydney and Southern Highland regions of NSW. We offer a 24 hour emergency service for piece of mind to our customers. Call us now to see how we can help you. Kelvane Plumbing approaches every job with attention to detail and excellent customer service. With our superior workmanship you can be confident that the job will be done right the first time around. You can rest assured with results that are guaranteed to last.

Target Market(s)

the general public

Contact Information for Business Card

look up website for some ideas something with similar colours to logo and new modern and to catch the eye.

Colors
fdfdfd
ffffff
000000
7f7f7f
aaaaaa
33a6d7
0492cd

Requirements
Must have
• all contact details
• company- Kelvane Plumbing
• name- Dashel Morrowby
• number mobile- 0431 906 154
• Email address- info@kelvaneplumbing.example
• Website- www.kelvaneplumbing.example
• ABN- 82 916 203 471
• LIC- 604517K

```html
<!DOCTYPE html>
<html lang="en">
<head>
<meta charset="utf-8">
<title>Kelvane Plumbing Business Cards</title>
<link href="https://fonts.googleapis.com/css2?family=Roboto:ital,wght@0,400;0,500;0,700;1,500&display=swap" rel="stylesheet">
<style>
  :root {
    --backdrop: #2a2d31;
    --card-black: #000000;
    --card-white: #ffffff;
    --ink: #000000;
    --grey: #7f7f7f;
    --grey-light: #aaaaaa;
    --blue: #33a6d7;
    --blue-deep: #0492cd;
  }
  * { box-sizing: border-box; margin: 0; padding: 0; }
  html, body { width: 1200px; height: 900px; overflow: hidden; }
  body {
    background: var(--backdrop);
    font-family: "Roboto", Arial, sans-serif;
    display: flex;
    flex-direction: column;
    align-items: center;
    justify-content: center;
    gap: 48px;
  }
  .card {
    position: relative;
    width: 600px;
    height: 343px;
    border-radius: 22px;
    overflow: hidden;
    box-shadow: 0 12px 30px rgba(0,0,0,0.45);
  }

  /* Front */
  .card-front { background: var(--card-black); color: var(--card-white); }
  .brand {
    position: absolute;
    top: 70px; left: 0; right: 0;
    display: flex; align-items: center; justify-content: center; gap: 16px;
  }
  .brand-dot {
    width: 44px; height: 44px; border-radius: 50%;
    border: 5px solid var(--blue);
  }
  .brand-name {
    font-weight: 700; font-size: 40px; color: var(--blue);
    letter-spacing: 1px; text-transform: uppercase;
  }
  .services {
    position: absolute;
    left: 0; right: 0; bottom: 52px;
    display: flex; justify-content: center; align-items: center; gap: 22px;
    font-size: 21px; font-weight: 400; color: var(--card-white);
  }
  .services .divider { color: var(--blue); font-weight: 500; }

  /* Back */
  .card-back { background: var(--card-white); color: var(--ink); }
  .top-band {
    position: absolute; top: 0; left: 0;
    width: 430px; height: 16px;
    background: var(--blue);
    clip-path: polygon(0 0, 100% 0, 96% 100%, 0 100%);
  }
  .holder-name {
    position: absolute; top: 44px; left: 44px;
    font-size: 27px; font-weight: 700; font-style: italic;
  }
  .registration {
    position: absolute; top: 92px; left: 44px;
    font-size: 14px; font-weight: 500; line-height: 1.4;
  }
  .contacts {
    position: absolute; top: 150px; left: 44px;
    list-style: none; display: flex; flex-direction: column; gap: 12px;
    font-size: 15px; font-weight: 500;
  }
  .contacts li { display: flex; align-items: center; gap: 10px; }
  .contacts svg { width: 20px; height: 20px; flex: none; }
  .mark {
    position: absolute; right: 40px; top: 96px;
    display: flex; align-items: center; gap: 12px;
  }
  .mark-dot { width: 38px; height: 38px; border-radius: 50%; background: var(--blue); }
  .mark-name { font-size: 26px; font-weight: 700; color: var(--blue); }
  .tagline {
    position: absolute; right: 40px; bottom: 34px;
    font-size: 16px; font-weight: 500; font-style: italic;
  }
</style>
</head>
<body>
  <section class="card card-front" aria-label="Business card front">
    <div class="brand">
      <span class="brand-dot"></span>
      <span class="brand-name">Kelvane Plumbing</span>
    </div>
    <p class="services">
      <span>Plumbing</span><span class="divider">/</span>
      <span>Drainage</span><span class="divider">/</span>
      <span>Gasfitting</span><span class="divider">/</span>
      <span>Roofing</span>
    </p>
  </section>

  <section class="card card-back" aria-label="Business card back">
    <div class="top-band"></div>
    <h1 class="holder-name">Dashel Morrowby</h1>
    <p class="registration">ABN- 82 916 203 471<br>LIC- 604517K</p>
    <ul class="contacts">
      <li>
        <svg viewBox="0 0 24 24" aria-hidden="true"><path fill="var(--blue-deep)" d="M6.6 10.8a15.1 15.1 0 0 0 6.6 6.6l2.2-2.2c.3-.3.7-.4 1-.2 1.1.4 2.3.6 3.6.6.6 0 1 .4 1 1V20c0 .6-.4 1-1 1A17 17 0 0 1 3 4c0-.6.4-1 1-1h3.5c.6 0 1 .4 1 1 0 1.3.2 2.5.6 3.6.1.3 0 .7-.2 1z"/></svg>
        <span>0431 906 154</span>
      </li>
      <li>
        <svg viewBox="0 0 24 24" aria-hidden="true"><rect x="2" y="5" width="20" height="14" rx="1.5" fill="var(--blue-deep)"/><path d="M3 6l9 7 9-7" fill="none" stroke="#fff" stroke-width="1.6"/></svg>
        <span>info@kelvaneplumbing.example</span>
      </li>
      <li>
        <svg viewBox="0 0 24 24" aria-hidden="true"><g fill="none" stroke="var(--blue-deep)" stroke-width="1.8"><circle cx="12" cy="12" r="9.5"/><ellipse cx="12" cy="12" rx="4" ry="9.5"/><path d="M2.5 12h19M4 7h16M4 17h16"/></g></svg>
        <span>www.kelvaneplumbing.example</span>
      </li>
    </ul>
    <div class="mark">
      <span class="mark-dot"></span>
      <span class="mark-name">Kelvane Plumbing</span>
    </div>
    <p class="tagline">Professional. Fast. Reliable.</p>
  </section>
</body>
</html>
```